Unique Elegant Stationary Set

Prepare a unique eye catching stationary set consisting of :
(1) Letterhead
(2) A3 Envelope
(3) Business Card
(4) Email Signature Banner

Package to be elegant, modern, and designers not only to think of design or colors but also materials could make a big difference, embossing, debossing, glossy, matt ....etc.

I attached both our new logos (Stacked or Linear) noting you may use any of them but you cant modify anything in the logos. Also attached our final draft portfolio to see what type of projects we work on and i also have here a glimboard page link showing the direction we want: https://www.glimboard.example/ravelkoton/business-card-design/

Target Market(s)

VVIP / Elite Developers

Industry/Entity Type

Architecture

Font styles to use
Sans Serif
Other font styles liked:
• unitext

Requirements
Should not have
• too many colors, or being busy in general. We want something pleasing to the eye

```html
<!DOCTYPE html>
<html lang="en">
<head>
<meta charset="utf-8">
<title>Norvale Design – Business Card</title>
<link rel="stylesheet" href="https://fonts.googleapis.com/css2?family=Lato:wght@400;700&display=swap">
<style>
  :root {
    --backdrop: #1f1f1f;
    --card: #2c2c2c;
    --card-frame: #434343;
    --ink: #f2f2f2;
    --ink-soft: #d8d8d8;
    --mark: #8a8a8a;
    --rule: #cfcfcf;
  }
  * { box-sizing: border-box; margin: 0; padding: 0; }
  html, body {
    width: 1200px; height: 694px; overflow: hidden;
    background: var(--backdrop);
    font-family: "Lato", sans-serif;
  }
  .stage {
    position: relative; width: 1200px; height: 694px;
    display: flex; align-items: center; justify-content: center; gap: 44px;
  }
  .card {
    position: relative; width: 540px; height: 309px;
    background: var(--card);
    box-shadow: 0 18px 40px rgba(0,0,0,.45);
  }
  /* Brand wordmark set as plain text */
  .wordmark {
    display: flex; align-items: center; gap: 12px;
    color: var(--mark);
    font-weight: 700; text-transform: uppercase; letter-spacing: .22em;
  }
  .wordmark__square { width: 18px; height: 18px; background: var(--mark); flex: none; }
  .card--front { display: flex; align-items: center; justify-content: center; }
  .card--front .wordmark { font-size: 30px; }

  .card--back { background: var(--card-frame); padding: 10px; }
  .card__panel { position: relative; width: 100%; height: 100%; background: var(--card); }
  .card--back .wordmark {
    position: absolute; top: 30px; right: 30px; font-size: 17px; gap: 9px;
  }
  .card--back .wordmark__square { width: 12px; height: 12px; }
  .rule { position: absolute; height: 1px; background: var(--rule); }
  .rule--long { left: 30px; right: 30px; top: 78px; }
  .rule--short { left: 30px; width: 190px; top: 160px; }

  .person { position: absolute; left: 30px; top: 104px; color: var(--ink); }
  .person__name { font-size: 20px; font-weight: 700; letter-spacing: .01em; }
  .person__role { font-size: 13px; color: var(--ink-soft); margin-top: 4px; }

  .contacts { position: absolute; left: 30px; top: 176px; list-style: none; }
  .contacts__item {
    display: flex; align-items: center; gap: 10px;
    font-size: 13px; color: var(--ink); line-height: 1; margin-bottom: 11px;
  }
  .contacts__icon { width: 14px; height: 14px; flex: none; fill: var(--ink); }

  .address {
    position: absolute; right: 30px; top: 104px;
    text-align: right; font-size: 13px; line-height: 1.55; color: var(--ink-soft);
  }
</style>
</head>
<body>
<main class="stage">
  <section class="card card--front" aria-label="Business card front">
    <div class="wordmark"><span class="wordmark__square"></span>Norvale Design</div>
  </section>

  <section class="card card--back" aria-label="Business card back">
    <div class="card__panel">
      <div class="wordmark"><span class="wordmark__square"></span>Norvale Design</div>
      <div class="rule rule--long"></div>

      <div class="person">
        <p class="person__name">ELIAS MARROW</p>
        <p class="person__role">Managing Director</p>
      </div>
      <div class="rule rule--short"></div>

      <address class="address">
        421, Address line goes here<br>45452, Country name
      </address>

      <ul class="contacts">
        <li class="contacts__item">
          <svg class="contacts__icon" viewBox="0 0 24 24" aria-hidden="true"><path d="M6.6 10.8a15.1 15.1 0 0 0 6.6 6.6l2.2-2.2c.3-.3.7-.4 1-.2 1.1.4 2.3.6 3.6.6.6 0 1 .4 1 1V20c0 .6-.4 1-1 1A17 17 0 0 1 3 4c0-.6.4-1 1-1h3.5c.6 0 1 .4 1 1 0 1.3.2 2.5.6 3.6.1.3 0 .7-.2 1z"/></svg>
          044-123 456 789
        </li>
        <li class="contacts__item">
          <svg class="contacts__icon" viewBox="0 0 24 24" aria-hidden="true"><path d="M2 5h20v14H2z M2 5l10 8 10-8" fill="none" stroke="#f2f2f2" stroke-width="2"/></svg>
          info@webname.com
        </li>
        <li class="contacts__item">
          <svg class="contacts__icon" viewBox="0 0 24 24" aria-hidden="true"><circle cx="12" cy="12" r="9" fill="none" stroke="#f2f2f2" stroke-width="2"/><path d="M3 12h18M12 3c3 3 3 15 0 18M12 3c-3 3-3 15 0 18" fill="none" stroke="#f2f2f2" stroke-width="1.6"/></svg>
          www.websitename.com
        </li>
      </ul>
    </div>
  </section>
</main>
</body>
</html>
```